Brivane - Business Cards for a new venture

create business card for a startup classified business dealing in construction materials, the cards need to have a professional look but modern, more serious than playful, one of the samples must include the official font (attached), please explore using the official colors in the company's logo

Target Market(s)

Energy sector

Contact Information for Business Card

Font styles to use
Other font styles liked:
• suissnord

Requirements
Must have
• corporate colors (in logo attached)
Nice to have
• Official font (in one of the samples) font is : suissnord
Should not have
• Cartoonish look

```html
<!DOCTYPE html>
<html lang="en">
<head>
<meta charset="utf-8">
<title>Brivane Business Cards</title>
<link rel="stylesheet" href="https://fonts.googleapis.com/css2?family=Michroma&family=Roboto:wght@400;700&display=swap">
<style>
  :root {
    --stage: #2a2a2c;
    --navy: #1d3c78;
    --navy-deep: #152d5e;
    --band: #0f4a80;
    --band-line: #ffffff;
    --paper: #f4f5f7;
    --steel: #8a8d93;
    --ink-light: #e3e8f0;
  }
  * { box-sizing: border-box; margin: 0; padding: 0; }
  html, body {
    width: 1200px; height: 997px; overflow: hidden;
    background: var(--stage);
  }
  .stage {
    position: relative; width: 1200px; height: 997px;
    display: flex; align-items: center; justify-content: center; gap: 40px;
  }
  .card {
    position: relative; width: 540px; height: 309px; overflow: hidden;
    box-shadow: 0 10px 30px rgba(0,0,0,.45);
  }

  /* Back side */
  .card-back { background: var(--navy); }
  .card-back .facet-field {
    position: absolute; inset: 0;
    background: linear-gradient(135deg, var(--navy) 0%, var(--navy-deep) 55%, #24488c 100%);
  }
  .card-back .brand {
    position: absolute; right: 42px; top: 128px; text-align: left;
  }
  .card-back .wordmark {
    font-family: "Michroma", sans-serif; font-size: 38px; letter-spacing: 2px;
    color: #ffffff; line-height: 1;
  }
  .card-back .web {
    margin-top: 10px;
    font-family: "Roboto", sans-serif; font-size: 11px; letter-spacing: 6px;
    color: var(--ink-light);
  }

  /* Front side */
  .card-front { background: var(--paper); }
  .card-front .mark {
    position: absolute; left: 0; right: 0; top: 48px;
    display: flex; flex-direction: column; align-items: center; gap: 14px;
  }
  .card-front .mark-dot {
    width: 38px; height: 38px; border-radius: 50%; background: var(--navy);
  }
  .card-front .wordmark {
    font-family: "Michroma", sans-serif; font-size: 26px; letter-spacing: 2px;
    color: var(--steel); line-height: 1;
  }
  .card-front .band-rules {
    position: absolute; left: 0; right: 0; top: 160px; height: 14px;
  }
  .card-front .band-rules span {
    position: absolute; left: 0; right: 0; height: 2px; background: var(--band);
  }
  .card-front .band-rules span:nth-child(1) { top: 0; }
  .card-front .band-rules span:nth-child(2) { top: 6px; }
  .card-front .band {
    position: absolute; left: 0; right: 0; top: 176px; bottom: 0; background: var(--band);
  }
  .card-front .person {
    position: absolute; left: 40px; bottom: 40px;
    font-family: "Roboto", sans-serif; color: var(--ink-light);
  }
  .card-front .person-name { font-size: 19px; font-weight: 700; }
  .card-front .person-org { font-size: 12px; margin-top: 3px; padding-left: 60px; }
  .card-front .divider {
    position: absolute; left: 284px; top: 196px; width: 1px; height: 90px;
    background: rgba(255,255,255,.7);
  }
  .card-front .contacts {
    position: absolute; left: 308px; top: 198px; list-style: none;
    font-family: "Roboto", sans-serif; font-size: 13px; color: var(--ink-light);
  }
  .card-front .contacts li {
    display: flex; align-items: center; gap: 12px; height: 26px;
  }
  .card-front .contacts svg { width: 14px; height: 14px; flex: none; }
</style>
</head>
<body>
<main class="stage">

  <section class="card card-back">
    <div class="facet-field" role="img" aria-label="Faceted navy polygon background pattern"></div>
    <div class="brand">
      <div class="wordmark">BRIVANE</div>
      <div class="web">www.brivane.com</div>
    </div>
  </section>

  <section class="card card-front">
    <div class="mark">
      <div class="mark-dot"></div>
      <div class="wordmark">BRIVANE</div>
    </div>
    <div class="band-rules"><span></span><span></span></div>
    <div class="band"></div>
    <div class="person">
      <div class="person-name">Helena Marsh</div>
      <div class="person-org">Norvel Advisors</div>
    </div>
    <div class="divider"></div>
    <ul class="contacts">
      <li>
        <svg viewBox="0 0 16 16" fill="#e3e8f0"><path d="M2 5c0-2 2-3 6-3s6 1 6 3l-3 1-1-2H6L5 6 2 5zm2 2h8l2 6H2l2-6zm4 1.5a2 2 0 100 4 2 2 0 000-4z"/></svg>
        <span>(555) 210-4837</span>
      </li>
      <li>
        <svg viewBox="0 0 16 16" fill="none" stroke="#e3e8f0" stroke-width="1.5"><rect x="4.5" y="1.5" width="7" height="13" rx="1.2"/><line x1="7" y1="12" x2="9" y2="12"/></svg>
        <span>(555) 364-9120</span>
      </li>
      <li>
        <svg viewBox="0 0 16 16" fill="none" stroke="#e3e8f0" stroke-width="1.5"><rect x="1.5" y="3.5" width="13" height="9"/><path d="M1.5 3.5L8 9l6.5-5.5"/></svg>
        <span>hmarsh@brivane.com</span>
      </li>
    </ul>
  </section>

</main>
</body>
</html>
```